Bright-Harbor Ledger Development, a residential real estate development company, needs a logo / busine

logo & business card design is needed for a new company based in Dallas, TX.
Name: Bright-Harbor Ledger Development, LLC (BHL Development)
We are a residential real estate development company seeking to change neighborhoods one house at a time. Providing individuals and families homes in a neighborhood community where they want to live rather the mcmansion developments we've seen developed the past couple of decades.
The final design should be simplistic, professional and convey a unique, but sophisticated image.

info for the business card:

Norah T. Pellow
President

address: P.O. Box 40371, Dallas, TX 75219
phone: 214.555.3172
email: npellow@bhl-ventrix.com

Residential

Requirements
Should not have
• No black in the design (i.e stripes, waves etc. ok for the font)

```html
<!DOCTYPE html>
<html lang="en">
<head>
<meta charset="utf-8">
<title>BHL Development – Business Card</title>
<link href="https://fonts.googleapis.com/css2?family=Montserrat:ital,wght@0,400;0,500;0,700;1,400&display=swap" rel="stylesheet">
<style>
  :root {
    --orange: #f26a44;
    --slate: #6d6e70;
    --ink: #3d3d3f;
    --paper: #ffffff;
    --backdrop: #ffffff;
  }
  html, body {
    margin: 0;
    padding: 0;
    width: 1200px;
    height: 1000px;
    overflow: hidden;
    background: var(--backdrop);
    font-family: "Montserrat", sans-serif;
    color: var(--ink);
  }
  .canvas {
    position: relative;
    width: 1200px;
    height: 1000px;
  }
  .card {
    position: absolute;
    background: var(--paper);
    box-shadow: 0 6px 18px rgba(0,0,0,0.22);
    overflow: hidden;
  }
  .card-front { left: 359px; top: 138px; width: 482px; height: 295px; }
  .card-back  { left: 360px; top: 477px; width: 480px; height: 293px; }
  .card svg.shape { position: absolute; left: 0; top: 0; }

  .wordmark {
    position: absolute;
    display: flex;
    align-items: center;
    white-space: nowrap;
    font-weight: 400;
    color: var(--ink);
  }
  .wordmark .mark-square { background: var(--slate); flex: none; }

  .front-wordmark { left: 65px; top: 64px; font-size: 33px; }
  .front-wordmark .mark-square { width: 33px; height: 34px; margin-right: 14px; }

  .back-wordmark { left: 202px; top: 238px; font-size: 20px; }
  .back-wordmark .mark-square { width: 21px; height: 22px; margin-right: 10px; }

  .hero-wordmark { left: 540px; top: 878px; font-size: 48px; }
  .hero-wordmark .mark-square { width: 49px; height: 49px; margin-right: 20px; }

  .contact {
    position: absolute;
    left: 60px;
    top: 36px;
  }
  .contact .pointer { position: absolute; left: -20px; top: 0; }
  .contact .name {
    margin: 0;
    font-size: 15px;
    font-weight: 700;
    letter-spacing: 0.06em;
    line-height: 20px;
  }
  .contact .title {
    margin: 0;
    font-size: 12.5px;
    font-style: italic;
    line-height: 17px;
    color: var(--slate);
  }
  .contact .address {
    margin: 6px 0 0;
    font-size: 14.5px;
    line-height: 19px;
    font-style: normal;
  }
  .contact .phone {
    margin: 8px 0 0;
    font-size: 15px;
    font-weight: 700;
    letter-spacing: 0.04em;
    line-height: 18px;
  }
  .contact .email {
    margin: 0;
    font-size: 12.5px;
    line-height: 16px;
  }
</style>
</head>
<body>
<main class="canvas">

  <section class="card card-front" aria-label="Business card front">
    <svg class="shape" width="482" height="295" viewBox="0 0 482 295" aria-hidden="true">
      <polygon points="0,169 482,295 0,295" fill="var(--orange)"/>
    </svg>
    <div class="wordmark front-wordmark">
      <span class="mark-square"></span>
      <span class="wordmark-text">BHL Development</span>
    </div>
  </section>

  <section class="card card-back" aria-label="Business card back">
    <svg class="shape" width="480" height="293" viewBox="0 0 480 293" aria-hidden="true">
      <polygon points="480,0 405,74 480,149" fill="var(--orange)"/>
    </svg>
    <div class="contact">
      <svg class="pointer" width="12" height="22" viewBox="0 0 12 22" aria-hidden="true">
        <polygon points="0,0 12,11 0,22" fill="var(--orange)"/>
      </svg>
      <p class="name">NORAH T. PELLOW</p>
      <p class="title">President</p>
      <address class="address">P.O. Box 40371,<br>Dallas, TX 75219</address>
      <p class="phone">xxx.xxx.xxxx</p>
      <p class="email">npellow@bhl-ventrix.com</p>
    </div>
    <div class="wordmark back-wordmark">
      <span class="mark-square"></span>
      <span class="wordmark-text">BHL Development</span>
    </div>
  </section>

  <div class="wordmark hero-wordmark">
    <span class="mark-square"></span>
    <span class="wordmark-text">BHL Development</span>
  </div>

</main>
</body>
</html>
```